Update Product Descriptions on Existing Website

We need to update product descriptions and images on three pages of our existing website. The tables are in editable HTML format. The formatting will be the exact same, just need the descriptions and images updated.

I have included the source documents below.

Coding

Coded - Design and coding required

Number of Pages Required

3 page

Colors

Designer to choose colors to be used in the design.

```html
<!DOCTYPE html>
<html lang="en">
<head>
<meta charset="utf-8">
<title>Molded Grating Sizes</title>
<link href="https://fonts.googleapis.com/css2?family=Roboto:wght@300;400&display=swap" rel="stylesheet">
<style>
  :root {
    --page-bg: #f7f7f6;
    --cell-bg: #f7f7f6;
    --text: #555555;
    --rule: #b9b9b9;
    --thumb-bg: #ffffff;
    --grate-dark: #2f6f5a;
    --grate-light: #5e9c86;
  }
  * { box-sizing: border-box; margin: 0; padding: 0; }
  html, body {
    width: 1200px;
    height: 675px;
    overflow: hidden;
    background: var(--page-bg);
    font-family: "Roboto", Arial, sans-serif;
    font-weight: 300;
    color: var(--text);
  }
  .catalog {
    width: 1200px;
    height: 675px;
    padding-top: 24px;
  }
  .catalog-intro {
    text-align: center;
    font-size: 12px;
    line-height: 16px;
    margin-bottom: 17px;
  }
  .size-table {
    width: 1057px;
    margin-left: 71px;
    border-collapse: collapse;
    table-layout: fixed;
    background: var(--cell-bg);
    font-size: 12px;
  }
  .size-table td,
  .size-table th {
    border: 1px solid var(--rule);
    height: 23px;
    text-align: center;
    font-weight: 300;
  }
  .size-table th {
    text-align: left;
    padding-left: 14px;
  }
  .profile-row td,
  .profile-row th { height: 98px; }
  .profile-label { line-height: 22px; }
  .grate-thumb {
    display: block;
    width: 115px;
    height: 85px;
    margin: 0 auto;
    background: var(--thumb-bg);
    padding: 12px 14px;
  }
  .grate-fill {
    width: 100%;
    height: 100%;
    border-radius: 4px;
    background: linear-gradient(135deg, var(--grate-light), var(--grate-dark));
    opacity: 0.85;
  }
</style>
</head>
<body>
<main class="catalog">
  <p class="catalog-intro">The following sizes and types of molded grating are available from Northgate:</p>
  <table class="size-table">
    <colgroup>
      <col style="width:176px"><col><col><col><col><col>
    </colgroup>
    <tbody>
      <tr class="profile-row">
        <th class="profile-label">Profile Image<br>(click to enlarge)</th>
        <td><span class="grate-thumb"><span class="grate-fill" style="display:block" role="img" aria-label="Isometric drawing of green molded grating panel"></span></span></td>
        <td><span class="grate-thumb"><span class="grate-fill" style="display:block" role="img" aria-label="Isometric drawing of green molded grating panel"></span></span></td>
        <td><span class="grate-thumb"><span class="grate-fill" style="display:block" role="img" aria-label="Isometric drawing of green molded grating panel"></span></span></td>
        <td><span class="grate-thumb"><span class="grate-fill" style="display:block" role="img" aria-label="Isometric drawing of green molded grating panel"></span></span></td>
        <td><span class="grate-thumb"><span class="grate-fill" style="display:block" role="img" aria-label="Isometric drawing of green molded grating panel"></span></span></td>
      </tr>
      <tr><th>Height (in.)</th><td>0.5</td><td>0.5</td><td>0.5</td><td>0.75</td><td>1</td></tr>
      <tr><th>Mesh Size (in.)</th><td>2x2</td><td>1.5x1.5</td><td>0.75x.75 1.5x1.5</td><td>1.5x1.5</td><td>1.5x1.5</td></tr>
      <tr><th>Standard Panel Size(ft.)</th><td>12x4</td><td>12.4</td><td>12.5x4</td><td>12x4</td><td>10x4, 12x4</td></tr>
      <tr><th>Open Area</th><td>74%</td><td>72%</td><td>42%</td><td>69%</td><td>69%</td></tr>
      <tr><th>Weight (lbs./ft.)</th><td>1.02</td><td>1.33</td><td>2.15</td><td>1.88</td><td>2.52</td></tr>
      <tr class="profile-row">
        <th class="profile-label">Profile Image<br>(click to enlarge)</th>
        <td><span class="grate-thumb"><span class="grate-fill" style="display:block" role="img" aria-label="Isometric drawing of green molded grating panel"></span></span></td>
        <td><span class="grate-thumb"><span class="grate-fill" style="display:block" role="img" aria-label="Isometric drawing of green molded grating panel"></span></span></td>
        <td><span class="grate-thumb"><span class="grate-fill" style="display:block" role="img" aria-label="Isometric drawing of green molded grating panel"></span></span></td>
        <td><span class="grate-thumb"><span class="grate-fill" style="display:block" role="img" aria-label="Isometric drawing of green molded grating panel"></span></span></td>
        <td><span class="grate-thumb"><span class="grate-fill" style="display:block" role="img" aria-label="Isometric drawing of green molded grating panel"></span></span></td>
      </tr>
      <tr><th>Height (in.)</th><td>0.5</td><td>0.5</td><td>0.5</td><td>0.75</td><td>1</td></tr>
      <tr><th>Mesh Size (in.)</th><td>2x2</td><td>1.5x1.5</td><td>0.75x.75 1.5x1.5</td><td>1.5x1.5</td><td>1.5x1.5</td></tr>
      <tr><th>Standard Panel Size(ft.)</th><td>12x4</td><td>12.4</td><td>12.5x4</td><td>12x4</td><td>10x4, 12x4</td></tr>
      <tr><th>Open Area</th><td>74%</td><td>72%</td><td>42%</td><td>69%</td><td>69%</td></tr>
      <tr><th>Weight (lbs./ft.)</th><td>1.02</td><td>1.33</td><td>2.15</td><td>1.88</td><td>2.52</td></tr>
    </tbody>
  </table>
</main>
</body>
</html>
```